Stubby Cooler Design for Promotional Purposes

We require 2 or 3 designs for promotional items to give away to clients. We use stubby coolers and have some current designs, but would like some alternatives. I attach the current designs we have. We are thinking about something based around "The 19th Hole" which is terminology for where golfers go to have a drink and relax after playing 18 holes of golf

Target Market(s)

Golfers

Font styles to use
Sans Serif

Colors
abd036
9bcb3c

Requirements
Must have
• We need one design that appeals to young professional men, therefore tasteful images of beautiful ladies holding golf clubs or playing golf. No nudity or distasteful images. More sexy and provocative than rude
• Another design should be more generic to appeal to older and female golfers
• We are thinking about something based around "The 19th Hole"; which is terminology for where golfers go to have a drink and relax after playing 18 holes of golf

```html
<!DOCTYPE html>
<html lang="en">
<head>
<meta charset="utf-8">
<title>The 19th Hole – Stubby Cooler Banner</title>
<link rel="stylesheet" href="https://fonts.googleapis.com/css2?family=Open+Sans:wght@300;400;600;700;800&display=swap">
<style>
  :root{
    --page:#e4e4e4;
    --white:#ffffff;
    --green-dark:#0b6a2f;
    --green-light:#9bcb3c;
    --green-band:#abc93a;
    --grey-text:#3c3c3c;
    --icon:#555555;
    --photo-a:#8c8a5c;
    --photo-b:#c9c2a0;
    --photo-c:#5f7446;
  }
  *{margin:0;padding:0;box-sizing:border-box}
  html,body{width:853px;height:1200px;overflow:hidden;background:var(--page)}
  body{font-family:"Open Sans",Arial,sans-serif;position:relative}
  .banner{position:absolute;left:20px;top:419px;width:813px;height:362px;background:var(--white);overflow:hidden;box-shadow:0 18px 22px -14px rgba(0,0,0,.35)}
  .banner-art{position:absolute;inset:0;width:100%;height:100%}
  .brand{position:absolute;left:480px;width:333px;top:104px;text-align:center;color:var(--green-dark);font-weight:400}
  .brand-name{display:block;font-size:33px;letter-spacing:.5px;line-height:1;white-space:nowrap}
  .brand-tag{display:block;font-size:11px;letter-spacing:6px;margin-top:7px;white-space:nowrap}
  .band-title{position:absolute;left:489px;right:0;top:180px;height:68px;display:flex;align-items:center;justify-content:center;color:var(--white);font-size:42px;font-weight:300;line-height:1;white-space:nowrap}
  .band-title .word{font-weight:700;margin-left:11px}
  .band-title sup{font-size:22px;vertical-align:top;position:relative;top:-4px}
  .contact{position:absolute;left:463px;display:flex;align-items:center;gap:10px;white-space:nowrap;line-height:1}
  .contact svg{flex:none}
  .contact-phone{top:268px;color:var(--green-dark);font-size:40px;font-weight:800}
  .contact-web{top:314px;color:var(--grey-text);font-size:21px;font-weight:400;gap:12px;left:467px}
  .contact-web b{color:var(--green-band);font-weight:600}
</style>
</head>
<body>
  <section class="banner">
    <svg class="banner-art" viewBox="0 0 955 425" preserveAspectRatio="none">
      <defs>
        <linearGradient id="photoTone" x1="0" y1="0" x2="1" y2="1">
          <stop offset="0" stop-color="var(--photo-c)"/>
          <stop offset=".5" stop-color="var(--photo-b)"/>
          <stop offset="1" stop-color="var(--photo-a)"/>
        </linearGradient>
      </defs>
      <rect class="photo" role="img" aria-label="Photo of an older couple cheering with arms raised, one holding a golf putter, on a sunny course" x="0" y="0" width="700" height="425" fill="url(#photoTone)"/>
      <path class="panel" d="M625 0 C560 80 505 180 505 280 C505 340 520 390 545 425 L955 425 L955 0 Z" fill="var(--white)"/>
      <path class="swoosh-dark" d="M575 0 C520 70 470 170 478 270 C484 340 505 395 530 425 L545 425 C520 380 502 320 505 250 C510 160 560 70 590 0 Z" fill="var(--green-dark)"/>
      <path class="swoosh-light" d="M612 30 C560 110 530 190 532 270 C534 340 550 395 575 425 L585 425 C560 380 548 320 550 260 C553 180 585 100 612 30 Z" fill="var(--green-light)"/>
      <rect class="band" x="575" y="211" width="380" height="80" fill="var(--green-band)"/>
    </svg>

    <div class="brand">
      <span class="brand-name">FAIRWAY SOCIAL</span>
      <span class="brand-tag">GOLF TOURS</span>
    </div>

    <h1 class="band-title">The<span class="word">19<sup>th</sup></span><span class="word">Hole</span></h1>

    <p class="contact contact-phone">
      <svg width="22" height="22" viewBox="0 0 24 24" fill="none" stroke="var(--icon)" stroke-width="2" stroke-linecap="round" stroke-linejoin="round"><path d="M22 16.9v3a2 2 0 0 1-2.2 2 19.8 19.8 0 0 1-8.6-3.1 19.5 19.5 0 0 1-6-6A19.8 19.8 0 0 1 2.1 4.2 2 2 0 0 1 4.1 2h3a2 2 0 0 1 2 1.7c.1 1 .4 1.9.7 2.8a2 2 0 0 1-.5 2.1L8 9.9a16 16 0 0 0 6 6l1.3-1.3a2 2 0 0 1 2.1-.4c.9.3 1.8.6 2.8.7a2 2 0 0 1 1.7 2z"/></svg>
      <span>13000 555 019</span>
    </p>
    <p class="contact contact-web">
      <svg width="16" height="16" viewBox="0 0 24 24" fill="none" stroke="var(--icon)" stroke-width="2"><circle cx="12" cy="12" r="10"/><path d="M2 12h20M12 2c3 3 3 17 0 20M12 2c-3 3-3 17 0 20"/></svg>
      <span>www.<b>fairwaysocial</b>.com.au</span>
    </p>
  </section>
</body>
</html>
```